下記の商品のパッケージデザインをお願い致します。

【商品名】国産 赤なた豆茶
~楽しくなる毎日のために〜
【原 料】赤なた豆
【内容量】3g×30包 ←表示しなくてもいいです
【特 徴】
効果は蓄膿症、副鼻腔炎、花粉症、口臭、便秘、アレルギー…などなど、数多くの症状の改善に有効と言われている健康茶です。
ソラノハコというブランドでこちらの商品を販売します。

<要望事項>
1.添付のように水彩画風のデザインにしてください。
構図はほぼ同じでいいです。(文字フォントも同じように)
2.シールのサイズはW100×H160で考えています。
3.シールにブランドロゴを入れてください。ロゴは添付しておきます。
※パターンがいくつかありますので、デザインにあうものを使用して
頂ければと思います。
4.クラフト袋に包装予定です。シールを貼り付けたイメージ画像をご提案頂けるとありがたいです。

ご不明な点がありましたら、お気軽に質問下さい。
宜しくお願い致します。

デザインが一番イメージ通りだった

時間がない中たくさんのデザインをご提案頂きありがとうございます。
今後もシリーズで商品を出して行くので、ぜひたくさんのご提案を頂けましたら幸いです。宜しくお願い致します。

```html
<!DOCTYPE html>
<html lang="ja">
<head>
<meta charset="utf-8">
<title>赤なた豆茶 ラベル</title>
<link href="https://fonts.googleapis.com/css2?family=Yuji+Syuku&family=Zen+Maru+Gothic:wght@500;700&display=swap" rel="stylesheet">
<style>
  :root {
    --paper: #fbf8f1;
    --bean-red: #a82a2c;
    --title-red: #9e2326;
    --leaf-green: #7d9a4a;
    --leaf-light: #c4d49a;
    --bean-light: #c9777a;
    --tag-yellow: #f4e37a;
    --ink: #4a3a30;
    --soft-ink: #8a7a6c;
    --logo-pink: #d6738a;
  }
  html, body {
    margin: 0;
    padding: 0;
    width: 775px;
    height: 1200px;
    overflow: hidden;
    background: var(--paper);
  }
  .label {
    position: relative;
    width: 775px;
    height: 1200px;
    background: var(--paper);
    overflow: hidden;
    font-family: "Zen Maru Gothic", sans-serif;
    color: var(--ink);
  }
  .pod-illustration {
    position: absolute;
    left: 330px;
    top: 0;
    width: 445px;
    height: 800px;
    background: radial-gradient(ellipse at 60% 40%, var(--leaf-green) 0%, var(--leaf-light) 55%, rgba(251,248,241,0) 75%);
    opacity: 0.85;
  }
  .bean-illustration {
    position: absolute;
    left: 40px;
    top: 840px;
    width: 700px;
    height: 260px;
    background: radial-gradient(ellipse at 50% 50%, var(--bean-red) 0%, var(--bean-light) 50%, rgba(251,248,241,0) 75%);
    opacity: 0.85;
  }
  .tagline {
    position: absolute;
    left: 258px;
    top: 30px;
    writing-mode: vertical-rl;
    font-family: "Yuji Syuku", serif;
    font-size: 34px;
    letter-spacing: 4px;
    color: var(--title-red);
    background: linear-gradient(to right, transparent 10%, var(--tag-yellow) 10%, var(--tag-yellow) 90%, transparent 90%);
    padding: 10px 6px;
  }
  .product-title {
    position: absolute;
    font-family: "Yuji Syuku", serif;
    color: var(--title-red);
    writing-mode: vertical-rl;
    line-height: 1;
    margin: 0;
    font-weight: 400;
  }
  .title-first {
    left: 60px;
    top: 140px;
    font-size: 175px;
  }
  .title-second {
    left: 240px;
    top: 440px;
    font-size: 175px;
  }
  .origin-badge {
    position: absolute;
    left: 535px;
    top: 250px;
    width: 78px;
    height: 210px;
    background: var(--bean-red);
    border-radius: 10px;
    color: var(--paper);
    writing-mode: vertical-rl;
    font-family: "Yuji Syuku", serif;
    font-size: 58px;
    display: flex;
    align-items: center;
    justify-content: center;
    letter-spacing: 8px;
  }
  .romaji {
    position: absolute;
    left: 470px;
    top: 810px;
    font-size: 18px;
    letter-spacing: 3px;
    color: var(--soft-ink);
  }
  .brand {
    position: absolute;
    left: 40px;
    top: 1105px;
    display: flex;
    align-items: center;
    gap: 10px;
    font-size: 26px;
    font-weight: 700;
    color: var(--logo-pink);
  }
  .brand-dot {
    width: 34px;
    height: 34px;
    border-radius: 50%;
    background: var(--logo-pink);
  }
  .net-content {
    position: absolute;
    left: 365px;
    top: 1090px;
    width: 120px;
    border: 2px solid var(--soft-ink);
    text-align: center;
    padding: 6px 0;
    font-size: 16px;
    line-height: 1.5;
    color: var(--ink);
  }
</style>
</head>
<body>
  <div class="label">
    <div class="pod-illustration" role="img" aria-label="水彩で描かれた赤なた豆のさやと葉"></div>
    <div class="bean-illustration" role="img" aria-label="水彩で描かれた赤なた豆の粒"></div>

    <p class="tagline">楽しくなる毎日のために</p>
    <h1 class="product-title title-first">赤なた</h1>
    <p class="product-title title-second">豆茶</p>

    <div class="origin-badge">国産</div>
    <p class="romaji">AKANATAMAME-CHA</p>

    <div class="brand"><span class="brand-dot"></span><span>ソラノハコ</span></div>
    <div class="net-content">内容量<br>90g (3g×30包)</div>
  </div>
</body>
</html>
```